Clean and modern business cards

Looking for an updated business card design for my dental office “tovrelle dental” . Looking for a modern clean / sleek design . I’m thinking black background but open to seeing other options . One side needs to have an appointment card . Card needs to have logo, dentist name , phone, email , address . I’ve attached couple of cards I thought were cool as well as my logo
Target Market(s)
Dental patients
Industry/Entity Type
Dentistry
Contact Information for Business Card
Phone email address

```html
<!DOCTYPE html>
<html lang="en">
<head>
<meta charset="utf-8">
<title>Tovrelle Dental – Business Cards</title>
<link rel="stylesheet" href="https://fonts.googleapis.com/css2?family=Open+Sans:wght@400;600;700&display=swap">
<style>
  :root {
    --page: #e9e6e1;
    --ink: #0b0b0b;
    --paper: #ffffff;
    --gold: #f2c230;
    --coral: #e8532b;
    --leaf: #8cc63f;
    --plum: #6a3d9a;
    --mist: #cfcfcf;
  }
  * { margin: 0; padding: 0; box-sizing: border-box; }
  html, body { width: 1200px; height: 900px; overflow: hidden; }
  body {
    background: var(--page);
    font-family: "Open Sans", Arial, sans-serif;
    position: relative;
  }
  .card {
    position: absolute;
    left: 250px;
    width: 700px;
    height: 400px;
    border-radius: 34px;
    overflow: hidden;
    box-shadow: 0 10px 28px rgba(0,0,0,.22);
  }
  /* Appointment side */
  .card--appointment { top: 40px; background: var(--paper); }
  .appointment__header {
    height: 222px;
    background: var(--ink);
    border-bottom: 4px solid var(--gold);
    color: var(--paper);
    text-align: center;
    padding-top: 44px;
  }
  .brand {
    display: inline-flex;
    align-items: center;
    gap: 14px;
    font-weight: 700;
    font-size: 40px;
    letter-spacing: 1px;
    text-transform: uppercase;
    color: var(--paper);
  }
  .brand__dot {
    width: 54px; height: 54px;
    border-radius: 50%;
    background: var(--gold);
  }
  .contact { margin-top: 22px; font-size: 15px; line-height: 1.75; }
  .contact__label { color: var(--coral); }
  .contact__sep { color: var(--gold); padding: 0 6px; }
  .appointment__body { padding: 26px 48px 0; text-align: center; }
  .appointment__title {
    color: var(--coral);
    font-weight: 700;
    font-size: 24px;
  }
  .appointment__fields {
    display: flex;
    gap: 28px;
    margin-top: 18px;
    text-align: left;
  }
  .field {
    flex: 1;
    display: flex;
    align-items: flex-end;
    gap: 10px;
    color: var(--leaf);
    font-weight: 700;
    font-size: 20px;
  }
  .field__line { flex: 1; border-bottom: 2px solid var(--leaf); margin-bottom: 6px; }
  .appointment__note {
    margin-top: 20px;
    color: var(--plum);
    font-size: 16px;
    line-height: 1.45;
  }
  /* Doctor side */
  .card--doctor { top: 460px; background: var(--ink); color: var(--paper); text-align: center; }
  .doctor__brand {
    margin-top: 92px;
    display: inline-flex;
    align-items: center;
    gap: 16px;
    font-weight: 700;
    font-size: 38px;
    letter-spacing: 3px;
    text-transform: uppercase;
  }
  .doctor__rule {
    width: 380px;
    height: 3px;
    background: var(--gold);
    margin: 62px auto 20px;
  }
  .doctor__name {
    font-weight: 700;
    font-size: 26px;
    letter-spacing: 1px;
    text-transform: uppercase;
  }
</style>
</head>
<body>

<section class="card card--appointment">
  <header class="appointment__header">
    <div class="brand"><span class="brand__dot"></span>Tovrelle Dental</div>
    <div class="contact">
      <p><span class="contact__label">P.</span> (204) 555 - 0187<span class="contact__sep">|</span><span class="contact__label">E.</span> hello@tovrelledental.ca</p>
      <p>210 – 480 Larkspur Ave, Winnipeg, MB R2K 3T4<span class="contact__sep">|</span><span class="contact__label">W.</span> tovrelledental.ca</p>
    </div>
  </header>
  <div class="appointment__body">
    <h2 class="appointment__title">Your Next Appointment is</h2>
    <div class="appointment__fields">
      <div class="field">Date <span class="field__line"></span></div>
      <div class="field">Time <span class="field__line"></span></div>
    </div>
    <p class="appointment__note">To cancel or reschedule please notify us at least<br>48 hours prior to your scheduled appointment.</p>
  </div>
</section>

<section class="card card--doctor">
  <div class="doctor__brand"><span class="brand__dot"></span>Tovrelle Dental</div>
  <div class="doctor__rule"></div>
  <p class="doctor__name">Dr. Mirek Halvorsen</p>
</section>

</body>
</html>
```